New clean and fresh corporate PPT template for Telecom equipment maker

KVR (VELMAQ KVRT) is a telecom equipment maker in Silicon Valley. Our current PPT template that goes with http://morelintek.com is overbuilt, dark, huge in file size, and looks the opposite of fresh and clean.
Our new microsite @ http://investor-kvrt.com is the direction we want to go. We are B2B, selling to telecom operators, but still want something that looks clean and fresh and not stuffy, hence primarily white background with maximum whitespace in 16:9 format.
Style guidelines attached, exclusive use of approved colors required, the master should remain as simple as possible, and we want the file size to stay reasonable (i.e. less is better). Features we would like include:
- Lato font built-in to the template
- Text boxes with standard size fonts, that automatically get smaller with indention
- An interesting bullet style, nothing crazy, but with visual interest
- A pre-selected table format that is clean and allows for high-density tables with many rows & columns
- Whichever standard slides layouts in the master you think would help result in slides that are found in the current deck, without someone needing to build their own slide

```html
<!DOCTYPE html>
<html lang="en">
<head>
<meta charset="utf-8">
<title>KVR Presentation Template</title>
<link href="https://fonts.googleapis.com/css2?family=Lato:wght@400;700;900&family=Montserrat:wght@600;700&display=swap" rel="stylesheet">
<style>
:root{
  --sheet:#d9d9d9;
  --white:#ffffff;
  --ink:#111111;
  --text:#444444;
  --muted:#8a8a8a;
  --blue:#1ba1e2;
  --blue-dark:#0e86c2;
  --line:#d5d5d5;
  --table-bg:#e8edf1;
}
*{box-sizing:border-box;margin:0;padding:0}
html,body{width:800px;height:1200px;overflow:hidden;background:var(--sheet);font-family:"Lato",sans-serif;color:var(--text)}
.sheet{position:relative;width:800px;height:1200px}
.slide{position:absolute;width:372px;height:209px;background:var(--white);overflow:hidden}
.col-a{left:24px}.col-b{left:404px}
.row-1{top:61px}.row-2{top:278px}.row-3{top:495px}.row-4{top:713px}.row-5{top:930px}

.footer-band{position:absolute;left:0;right:0;bottom:0;height:9px;background:linear-gradient(90deg,var(--blue-dark),var(--blue),var(--blue-dark));display:flex;align-items:center;padding:0 24px;font-size:2.6px;color:#e8f6ff}
.footer-band .legal{position:absolute;left:140px}
.footer-band .page{position:absolute;right:18px;font-size:5.5px;font-weight:700;color:var(--white)}

.slide-title{position:absolute;font-family:"Montserrat",sans-serif;font-weight:700;font-size:9.5px;color:var(--ink);letter-spacing:.1px;white-space:nowrap}
.slide-title::after{content:"";position:absolute;left:0;bottom:-5px;width:20px;height:2px;background:linear-gradient(90deg,var(--ink) 0 70%,var(--blue) 70% 100%)}

.corner-mark{position:absolute;top:8px;right:22px;font-weight:900;font-size:10px;color:#7a8a96;letter-spacing:.5px;opacity:.35}
.corner-mark.on-photo{color:var(--white);opacity:.8}

.brand-box{position:absolute;left:0;top:13px;width:95px;height:33px;background:var(--ink);display:flex;align-items:center;padding:0 12px}
.brand-box .name{font-weight:900;color:var(--white);font-size:15px;letter-spacing:.8px}

.photo{position:absolute}
.body-copy{position:absolute;font-size:4.2px;line-height:1.35;color:var(--text)}

/* Cover */
.cover-photo{left:0;top:0;width:372px;height:140px;background:linear-gradient(180deg,#6f7fa6 0%,#a99bb0 45%,#d9a27a 66%,#2a2a38 78%,#14141c 100%)}
.cover-accent{position:absolute;left:24px;top:140px;width:40px;height:2px;background:linear-gradient(90deg,var(--blue) 0 50%,var(--ink) 50%)}
.stats{position:absolute;top:152px;left:58px;display:flex}
.stat{width:57px;text-align:center;border-right:1px solid var(--line);padding:0 2px}
.stat:last-child{border-right:none;width:70px}
.stat svg{display:block;margin:0 auto 1px}
.stat .num{font-size:6.5px;color:var(--blue);font-weight:700}
.stat .lbl{font-size:5px;color:var(--muted);text-transform:uppercase;letter-spacing:.2px}
.hq{position:absolute;top:192px;width:100%;text-align:center;font-size:3.4px;color:var(--ink);font-weight:700}
.hq span{display:block;color:var(--blue);font-weight:400;margin-top:1px}

/* Bullets */
.bullet-list{position:absolute;left:47px;top:106px;list-style:none;font-size:5px;color:var(--text)}
.bullet-list li{position:relative;padding-left:7px;margin-bottom:4.4px}
.bullet-list li::before{content:"";position:absolute;left:0;top:1.2px;width:3px;height:3px;background:var(--blue);box-shadow:1px 1px 0 var(--ink)}

/* Table */
.data-table{position:absolute;left:68px;top:73px;width:244px;border-collapse:collapse;font-size:4.3px}
.data-table th{background:var(--blue);color:var(--white);font-weight:700;height:11px;padding:0 4px;text-align:center}
.data-table th:first-child{background:var(--ink)}
.data-table td{background:var(--table-bg);height:12.5px;text-align:center;color:var(--muted);border-left:1px solid #cdd6dd}
.data-table td:first-child{color:var(--text);border-left:none}
.data-table tr:last-child td{border-bottom:1px solid var(--blue-dark)}

/* Team */
.team-name{position:absolute;left:78px;top:108px;font-size:6px;color:var(--blue);font-weight:700}
.subtitle{position:absolute;font-size:5.6px;color:var(--blue);font-weight:700;text-transform:uppercase}

/* Feature columns */
.feature-title{position:absolute;font-size:7.2px;color:var(--blue);font-weight:400;text-transform:uppercase}

/* Contact */
.contact-panel{position:absolute;left:204px;top:0;width:140px;height:209px;background:var(--white)}
.contact-panel h2{position:absolute;left:31px;top:73px;font-family:"Montserrat",sans-serif;font-weight:600;font-size:11.5px;color:var(--ink)}
.contact-list{position:absolute;left:49px;top:95px;list-style:none;font-size:4.2px;color:var(--ink)}
.contact-list li{display:flex;align-items:center;gap:4px;height:12px}
</style>
</head>
<body>
<main class="sheet">

  <!-- Cover -->
  <section class="slide col-a row-1">
    <div class="photo cover-photo" role="img" aria-label="City skyline at dusk with lit towers"></div>
    <div class="brand-box"><span class="name">KVR</span></div>
    <div class="cover-accent"></div>
    <div class="stats">
      <div class="stat"><svg width="7" height="7" viewBox="0 0 10 10"><circle cx="5" cy="5" r="3.5" fill="none" stroke="#1ba1e2" stroke-width="1"/></svg><div class="num">1000+</div><div class="lbl">Customers</div></div>
      <div class="stat"><svg width="7" height="7" viewBox="0 0 10 10"><circle cx="5" cy="5" r="4" fill="none" stroke="#1ba1e2"/><path d="M1 5h8M5 1v8" stroke="#1ba1e2" stroke-width=".8"/></svg><div class="num">50+</div><div class="lbl">Countries</div></div>
      <div class="stat"><svg width="9" height="7" viewBox="0 0 12 10"><circle cx="3" cy="3" r="1.5" fill="#1ba1e2"/><circle cx="6" cy="3" r="1.5" fill="#1ba1e2"/><circle cx="9" cy="3" r="1.5" fill="#1ba1e2"/><path d="M1 9a2 2 0 0 1 4 0M4 9a2 2 0 0 1 4 0M7 9a2 2 0 0 1 4 0" stroke="#1ba1e2" fill="none" stroke-width=".9"/></svg><div class="num">700+</div><div class="lbl">Employees</div></div>
      <div class="stat"><svg width="9" height="7" viewBox="0 0 12 10"><rect x="1" y="2" width="10" height="6" fill="none" stroke="#1ba1e2"/><circle cx="6" cy="5" r="1.5" fill="#1ba1e2"/></svg><div class="num">~$250M in 2017</div><div class="lbl">Annual Revenue</div></div>
    </div>
    <p class="hq">HEADQUARTERED IN HARBOR CITY, CA (VELMAQ:KVRT)<span>WWW.MORELINTEK.COM</span></p>
  </section>

  <!-- Safe harbor -->
  <section class="slide col-b row-1">
    <div class="corner-mark">KVR</div>
    <h1 class="slide-title" style="left:24px;top:37px">SAFE HARBOR STATEMENT</h1>
    <p class="body-copy" style="left:24px;top:66px;width:334px;font-size:4px;text-align:justify">This presentation contains forward-looking statements that are subject to the safe harbors created under the Securities Act of 1933 and the Securities Exchange Act of 1934. Words such as "anticipate," "believe," "continue," "could," "estimate," "expect," "goal," "intend," "may," "plan," "project," "seek," "should," "target," "will," "would," variations of such words, and similar expressions are intended to identify forward-looking statements. In addition, forward-looking statements include, among others, statements that refer to financial estimates, projections of revenue, margins, expenses or other financial items. Readers are cautioned that actual results could differ materially from those expressed in or contemplated by the forward-looking statements. Factors that could cause actual results to differ include, but are not limited to, commercial acceptance of the Company's products; intense competition in the communications equipment market; the Company's ability to execute on its strategy and operating plans; and economic conditions specific to the communications, networking, internet and related industries. In addition, please refer to the risk factors contained in the Company's SEC filings available at www.sec.gov, including without limitation, the Company's annual report on Form 10-K and quarterly reports on Form 10-Q. Readers are cautioned not to place undue reliance on any forward-looking statements, which speak only as of the date on which they are made. The Company undertakes no obligation to update or revise any forward-looking statements for any reason.</p>
    <div class="footer-band"><span>www.morelintek.com</span><span class="legal">© 2018 Morelin Tek Solutions – Proprietary and Confidential</span><span class="page">12</span></div>
  </section>

  <!-- Text options -->
  <section class="slide col-a row-2">
    <div class="corner-mark">KVR</div>
    <h1 class="slide-title" style="left:24px;top:20px">TEXT OPTIONS</h1>
    <p class="body-copy" style="left:24px;top:70px;width:330px;font-size:6.6px;line-height:1.25;font-weight:700;color:var(--ink)">Lorem ipsum dolor sit amet, consectetur adipisicing elit, sed do eiusmod tempor incididunt ut labore et dolore magna aliqua. Ut enim ad minim veniam, quis nostrud exercitation ullamco laboris nisi ut aliquip ex ea commodo consequat.</p>
    <p class="body-copy" style="left:46px;top:110px;width:306px;font-size:5px">Lorem ipsum dolor sit amet, consectetur adipisicing elit, sed do eiusmod tempor incididunt ut labore et dolore magna aliqua. Ut enim ad minim veniam, quis nostrud exercitation ullamco laboris nisi ut aliquip ex ea commodo consequat.</p>
    <p class="body-copy" style="left:64px;top:145px;width:290px;font-size:3.9px;color:var(--muted)">Lorem ipsum dolor sit amet, consectetur adipisicing elit, sed do eiusmod tempor incididunt ut labore et dolore magna aliqua. Ut enim ad minim veniam, quis nostrud exercitation ullamco laboris nisi ut aliquip ex ea commodo consequat.</p>
    <div class="footer-band"><span>www.morelintek.com</span><span class="legal">© 2018 Morelin Tek Solutions – Proprietary and Confidential</span><span class="page">12</span></div>
  </section>

  <!-- Text with bullets -->
  <section class="slide col-b row-2">
    <div class="corner-mark">KVR</div>
    <h1 class="slide-title" style="left:24px;top:42px">TEXT WITH BULLETS</h1>
    <p class="body-copy" style="left:24px;top:68px;width:330px;font-size:5.4px;line-height:1.3">Lorem ipsum dolor sit amet, consectetur adipisicing elit, sed do eiusmod tempor incididunt ut labore et dolore magna aliqua. Ut enim ad minim veniam, quis nostrud exercitation ullamco laboris nisi ut aliquip ex ea commodo consequat. Duis aute irure dolor in reprehenderit in voluptate velit esse cillum dolore eu fugiat nulla pariatur.</p>
    <ul class="bullet-list">
      <li>Lorem ipsum dolor sit amet</li>
      <li>Ut enim ad minim veniam</li>
      <li>Incididunt ut labore et dolore magna</li>
      <li>Esse cillum dolore eu fugiat nulla pariatur</li>
      <li>Dolor in reprehenderit in voluptate</li>
      <li>Nisi ut aliquip ex ea</li>
    </ul>
    <div class="footer-band"><span>www.morelintek.com</span><span class="legal">© 2018 Morelin Tek Solutions – Proprietary and Confidential</span><span class="page">12</span></div>
  </section>

  <!-- Title with photo -->
  <section class="slide col-a row-3">
    <svg class="photo" width="372" height="209" viewBox="0 0 372 209" role="img" aria-label="Business handshake over a desk, tinted blue">
      <defs><linearGradient id="handshakeTint" x1="0" y1="0" x2="1" y2="1"><stop offset="0" stop-color="#8fd3f4"/><stop offset="1" stop-color="#1b8fcb"/></linearGradient></defs>
      <polygon points="260,0 372,0 372,200 136,200" fill="url(#handshakeTint)"/>
    </svg>
    <div class="corner-mark on-photo">KVR</div>
    <h1 class="slide-title" style="left:24px;top:35px">YOUR TITLE GOES HERE</h1>
    <p class="body-copy" style="left:48px;top:64px;width:132px;font-size:6.8px;line-height:1.22">Lorem ipsum dolor sit amet, consectetur adipisicing elit, sed do eiusmod tempor incididunt ut labore et dolore magna aliqua. Ut enim ad minim veniam, quis nostrud exercitation ullamco laboris nisi ut aliquip ex ea commodo consequat. Duis aute irure dolor in reprehenderit in voluptate velit esse cillum dolore eu fugiat nulla pariatur.</p>
    <div class="footer-band"><span>www.morelintek.com</span><span class="page">12</span></div>
  </section>

  <!-- Our team -->
  <section class="slide col-b row-3">
    <div class="photo" style="left:201px;top:0;width:171px;height:200px;background:linear-gradient(180deg,#2e3c5c 0%,#4b5572 35%,#c98a5c 55%,#1c2030 75%,#3a3f4c 100%)" role="img" aria-label="Waterfront city towers at twilight"></div>
    <div class="corner-mark on-photo">KVR</div>
    <h1 class="slide-title" style="left:32px;top:24px">OUR TEAM</h1>
    <div class="photo" style="left:78px;top:66px;width:40px;height:36px;background:linear-gradient(135deg,#d8dde2,#9aa3ab);border:1px solid var(--blue)" role="img" aria-label="Portrait photo of team member"></div>
    <p class="team-name">Jonathan Doe</p>
    <p class="body-copy" style="left:78px;top:118px;width:60px;font-size:4px">Lorem ipsum dolor sit amet, consectetur adipisicing elit, sed do eiusmod tempor incididunt ut labore et dolore magna aliqua.</p>
    <p class="body-copy" style="left:78px;top:150px;width:60px;font-size:4px">Ut enim ad minim veniam, quis nostrud exercitation ullamco laboris nisi ut aliquip ex ea consequat.</p>
    <div class="footer-band"><span>www.morelintek.com</span><span class="legal">© 2018 Morelin Tek Solutions – Proprietary and Confidential</span><span class="page">12</span></div>
  </section>

  <!-- Table -->
  <section class="slide col-a row-4">
    <div class="corner-mark">KVR</div>
    <h1 class="slide-title" style="left:32px;top:23px">TABLE SLIDE</h1>
    <table class="data-table">
      <thead><tr><th>Subheading one</th><th>Subheading two</th><th>Subheading three</th><th>Subheading four</th></tr></thead>
      <tbody>
        <tr><td>Lorem ipsum du sit</td><td>Dolor</td><td>Dolor</td><td>Dolor</td></tr>
        <tr><td>Lorem ipsum du sit</td><td>Dolor</td><td>Dolor</td><td>Dolor</td></tr>
        <tr><td>Lorem ipsum du sit</td><td>Dolor</td><td>Dolor</td><td>Dolor</td></tr>
        <tr><td>Lorem ipsum du sit</td><td>Dolor</td><td>Dolor</td><td>Dolor</td></tr>
        <tr><td>Lorem ipsum du sit</td><td>Dolor</td><td>Dolor</td><td>Dolor</td></tr>
      </tbody>
    </table>
    <div class="footer-band"><span>www.morelintek.com</span><span class="legal">© 2018 Morelin Tek Solutions – Proprietary and Confidential</span><span class="page">12</span></div>
  </section>

  <!-- Graph and text -->
  <section class="slide col-b row-4">
    <div class="corner-mark">KVR</div>
    <h1 class="slide-title" style="left:32px;top:19px">GRAPH AND TEXT</h1>
    <svg style="position:absolute;left:62px;top:58px" width="126" height="115" viewBox="0 0 126 115" role="img" aria-label="Bar chart with four categories">
      <rect x=".5" y=".5" width="125" height="114" fill="#fff" stroke="#e0e0e0"/>
      <g font-family="Lato,sans-serif" font-size="3" fill="#444">
        <line x1="8" y1="95" x2="118" y2="95" stroke="#bbb" stroke-width=".5"/>
        <g transform="translate(10,0)"><rect x="0" y="45" width="4" height="50" fill="#1ba1e2"/><rect x="5" y="72" width="4" height="23" fill="#cfcfcf"/><rect x="10" y="78" width="4" height="17" fill="#111"/><text x="1" y="100">Category 1</text></g>
        <g transform="translate(37,0)"><rect x="0" y="72" width="4" height="23" fill="#1ba1e2"/><rect x="5" y="45" width="4" height="50" fill="#cfcfcf"/><rect x="10" y="78" width="4" height="17" fill="#111"/><text x="0" y="100">Category 2</text></g>
        <g transform="translate(64,0)"><rect x="0" y="60" width="4" height="35" fill="#1ba1e2"/><rect x="5" y="66" width="4" height="29" fill="#cfcfcf"/><rect x="10" y="78" width="4" height="17" fill="#111"/><text x="0" y="100">Category 3</text></g>
        <g transform="translate(91,0)"><rect x="0" y="45" width="4" height="50" fill="#1ba1e2"/><rect x="5" y="66" width="4" height="29" fill="#cfcfcf"/><rect x="10" y="40" width="4" height="55" fill="#111"/><text x="0" y="100">Category 4</text></g>
        <rect x="10" y="107" width="3" height="3" fill="#1ba1e2"/><text x="15" y="110" fill="#1ba1e2">Title Text</text>
        <rect x="50" y="107" width="3" height="3" fill="#cfcfcf"/><text x="55" y="110" fill="#aaa">Title Text</text>
        <rect x="88" y="107" width="3" height="3" fill="#111"/><text x="93" y="110">Title Text</text>
      </g>
    </svg>
    <p class="subtitle" style="left:202px;top:69px">Subtitle goes here</p>
    <p class="body-copy" style="left:202px;top:79px;width:128px;font-size:3.9px">Lorem ipsum dolor sit amet, consectetur adipisicing elit, sed do eiusmod tempor incididunt ut labore et dolore magna aliqua. Ut enim ad minim veniam, quis nostrud exercitation ullamco laboris nisi ut aliquip ex ea commodo consequat. Duis aute irure dolor in reprehenderit in voluptate velit esse cillum dolore eu fugiat nulla pariatur. Excepteur sint occaecat cupidatat non proident, sunt in culpa qui officia deserunt mollit anim id est laborum. Sed ut perspiciatis unde omnis iste natus error sit voluptatem accusantium doloremque laudantium, totam rem aperiam, eaque ipsa quae ab illo inventore veritatis et quasi architecto beatae vitae dicta sunt explicabo.</p>
    <div class="footer-band"><span>www.morelintek.com</span><span class="legal">© 2018 Morelin Tek Solutions – Proprietary and Confidential</span><span class="page">12</span></div>
  </section>

  <!-- Two features -->
  <section class="slide col-a row-5">
    <div class="photo" style="left:0;top:0;width:372px;height:87px;background:linear-gradient(180deg,#5a4a2e 0%,#b89a5a 40%,#7d8a60 65%,#3a3324 100%)" role="img" aria-label="Modern office lobby interior"></div>
    <svg style="position:absolute;left:68px;top:103px" width="12" height="13" viewBox="0 0 12 13"><g fill="none" stroke="#1ba1e2" stroke-width=".8"><ellipse cx="6" cy="2.5" rx="5" ry="2"/><path d="M1 2.5v8c0 1.1 2.2 2 5 2s5-.9 5-2v-8M1 5.2c0 1.1 2.2 2 5 2s5-.9 5-2M1 7.9c0 1.1 2.2 2 5 2s5-.9 5-2"/></g></svg>
    <p class="feature-title" style="left:68px;top:121px">Place title text</p>
    <p class="body-copy" style="left:68px;top:132px;width:116px;font-size:3.7px">Lorem ipsum dolor sit amet, consectetur adipisicing elit, sed do eiusmod tempor incididunt ut labore et dolore magna aliqua. Ut enim ad minim veniam, quis nostrud exercitation ullamco laboris nisi ut aliquip ex ea commodo consequat. Duis aute irure dolor in reprehenderit in voluptate velit esse cillum dolore eu fugiat nulla pariatur. Excepteur sint occaecat cupidatat non proident, sunt in culpa qui officia deserunt mollit anim id est laborum.</p>
    <svg style="position:absolute;left:208px;top:104px" width="22" height="12" viewBox="0 0 22 12"><path d="M5 11a4 4 0 0 1 0-8 6 6 0 0 1 11 1 3.5 3.5 0 0 1 1 7z" fill="none" stroke="#1ba1e2" stroke-width=".8"/></svg>
    <p class="feature-title" style="left:209px;top:121px">Place title text</p>
    <p class="body-copy" style="left:209px;top:132px;width:116px;font-size:3.7px">Lorem ipsum dolor sit amet, consectetur adipisicing elit, sed do eiusmod tempor incididunt ut labore et dolore magna aliqua. Ut enim ad minim veniam, quis nostrud exercitation ullamco laboris nisi ut aliquip ex ea commodo consequat. Duis aute irure dolor in reprehenderit in voluptate velit esse cillum dolore eu fugiat nulla pariatur. Excepteur sint occaecat cupidatat non proident, sunt in culpa qui officia deserunt mollit anim id est laborum.</p>
    <div class="footer-band"><span>www.morelintek.com</span><span class="legal">© 2018 Morelin Tek Solutions – Proprietary and Confidential</span><span class="page">12</span></div>
  </section>

  <!-- Contact -->
  <section class="slide col-b row-5">
    <div class="photo" style="left:0;top:0;width:372px;height:209px;background:linear-gradient(180deg,#b9c3cc 0%,#9da8b6 30%,#5a5e6e 55%,#1c1c26 75%,#2b2a33 100%)" role="img" aria-label="City skyline across the water at night"></div>
    <div class="brand-box"><span class="name">KVR</span></div>
    <div class="contact-panel">
      <h2>Contact Us</h2>
      <ul class="contact-list">
        <li><svg width="6" height="6" viewBox="0 0 10 10"><path d="M2 1l2 2-1 1.5a6 6 0 0 0 2.5 2.5L7 6l2 2-1.5 1.5C4 9 1 6 .5 2.5z" fill="#1ba1e2"/></svg>(123) 456 7880</li>
        <li><svg width="6" height="6" viewBox="0 0 10 10"><circle cx="5" cy="5" r="4.3" fill="none" stroke="#1ba1e2"/><path d="M2.8 3.5h4.4v3H2.8zM2.8 3.5L5 5.2l2.2-1.7" fill="none" stroke="#1ba1e2" stroke-width=".7"/></svg>mail@website.com</li>
        <li><svg width="6" height="6" viewBox="0 0 10 10"><circle cx="5" cy="5" r="4.3" fill="none" stroke="#1ba1e2"/><path d="M1 5h8M5 .7c-2 2.5-2 6 0 8.6M5 .7c2 2.5 2 6 0 8.6" fill="none" stroke="#1ba1e2" stroke-width=".6"/></svg>www.morelintek.com</li>
        <li><svg width="6" height="6" viewBox="0 0 10 10"><path d="M5 9S2 5.8 2 3.8a3 3 0 0 1 6 0C8 5.8 5 9 5 9z" fill="none" stroke="#1ba1e2"/><circle cx="5" cy="3.8" r="1" fill="#1ba1e2"/></svg>Street No., Location</li>
      </ul>
      <div style="position:absolute;left:88px;bottom:0;width:52px;height:2px;background:linear-gradient(90deg,var(--blue) 0 25%,var(--ink) 25%)"></div>
    </div>
  </section>

</main>
</body>
</html>
```